Migration Lawyers

Company: Dunstan & Co Lawyers & Migration Agents

Name: Graham Dunstan BEc, LLB
Address: Level 18, 72 Hollis Street
Sydney, NSW, Australia 2000

Ph: +61 2 9384 5207
M: 0428316540
E: graham@permitpath-example.org.au
W: www.permitpath-example.org.au

Target Market(s)

Migration Clients

Industry/Entity Type

It Company

Font styles to use
Script

Requirements
Must have
• Logo
Should not have
• Please scale the format to the printing size attached

```html
<!DOCTYPE html>
<html lang="en">
<head>
<meta charset="utf-8">
<title>Dunstan &amp; Co Business Card</title>
<link rel="stylesheet" href="https://fonts.googleapis.com/css2?family=Tinos:wght@700&family=Alegreya:ital,wght@0,400;0,500;1,400&display=swap">
<style>
  :root {
    --stage: #e9e6e1;
    --card-dark: #050505;
    --card-light: #ffffff;
    --ink: #111111;
    --ink-soft: #444444;
    --silver: #e4e4e4;
    --ring-dark: #2a2a2a;
  }
  * { box-sizing: border-box; margin: 0; padding: 0; }
  html, body {
    width: 1200px; height: 1000px; overflow: hidden;
    background: var(--stage);
  }
  .card {
    position: absolute;
    left: 240px;
    width: 720px;
    height: 420px;
    box-shadow: 0 6px 18px rgba(0,0,0,0.25);
  }
  .card--front { top: 50px; background: var(--card-dark); }
  .card--back { top: 520px; background: var(--card-light); }

  .brand {
    position: absolute;
    text-align: center;
    font-family: "Tinos", "Times New Roman", serif;
    font-weight: 700;
  }
  .brand__mark { display: block; margin: 0 auto 22px; }
  .brand__name { font-size: 52px; line-height: 1; }
  .brand__tagline { font-size: 22px; line-height: 1.3; margin-top: 4px; }

  .card--front .brand { left: 0; right: 0; top: 58px; color: var(--silver); }
  .card--back .brand { left: 40px; width: 320px; top: 50px; color: var(--ink); }
  .card--back .brand__name { font-size: 44px; }
  .card--back .brand__tagline { font-size: 19px; }

  .contact {
    position: absolute;
    left: 398px; top: 44px;
    font-family: "Alegreya", Georgia, serif;
    color: var(--ink);
  }
  .contact__name { font-size: 32px; font-weight: 500; }
  .contact__creds { font-size: 16px; color: var(--ink-soft); margin-top: 6px; }
  .contact__list { list-style: none; margin-top: 40px; font-size: 17px; line-height: 1.75; }
  .contact__label { display: inline-block; width: 26px; color: var(--ink-soft); }
  .contact__address {
    font-style: italic; font-size: 18px; line-height: 1.65;
    color: var(--ink-soft); margin-top: 30px;
  }
  .card__band {
    position: absolute;
    right: 0; bottom: 0;
    width: 340px; height: 28px;
    background: var(--card-dark);
  }
</style>
</head>
<body>
  <section class="card card--front">
    <div class="brand">
      <svg class="brand__mark" width="150" height="150" viewBox="0 0 150 150" aria-hidden="true">
        <circle cx="75" cy="75" r="70" fill="none" stroke="var(--silver)" stroke-width="3"/>
      </svg>
      <div class="brand__name">Dunstan &amp; Co</div>
      <div class="brand__tagline">Lawyers &amp; Migration Agents</div>
    </div>
  </section>

  <section class="card card--back">
    <div class="brand">
      <svg class="brand__mark" width="140" height="140" viewBox="0 0 140 140" aria-hidden="true">
        <circle cx="70" cy="70" r="66" fill="none" stroke="var(--ring-dark)" stroke-width="3"/>
      </svg>
      <div class="brand__name">Dunstan &amp; Co</div>
      <div class="brand__tagline">Lawyers &amp; Migration Agents</div>
    </div>

    <div class="contact">
      <h1 class="contact__name">Graham Dunstan</h1>
      <p class="contact__creds">BEc, LLB</p>
      <ul class="contact__list">
        <li><span class="contact__label">P:</span>+61 2 9384 5207</li>
        <li><span class="contact__label">M:</span>0428316540</li>
        <li><span class="contact__label">E:</span>graham@permitpath-example.org.au</li>
        <li><span class="contact__label">W:</span>www.permitpath-example.org.au</li>
      </ul>
      <p class="contact__address">Level 18, 72 Hollis Street<br>Australia, Sydney, NSW, 2000</p>
    </div>
    <div class="card__band"></div>
  </section>
</body>
</html>
```